Business Card Design Project

for a second hand vintage clothing store. shop name is The Velvet Cupboard

Cards to be double sided

The name on the card is Joanna Whitfield

Information to put on card:

The Velvet Cupboard
Joanna Whitfield (no job title)
42/871 Dunmore St, Glenwick, Northvale, NSW, 2741.
Mobile: 0412 905 261
Email: thevelvetcupboard@mailbox.com.au
Web: www.thevelvetcupboard.com.au

Target Market(s)

Women looking at vintage clothing

Industry/Entity Type

Clothing

```html
<!DOCTYPE html>
<html lang="en">
<head>
<meta charset="utf-8">
<title>The Velvet Cupboard – Business Card</title>
<link rel="stylesheet" href="https://fonts.googleapis.com/css2?family=PT+Sans&display=swap">
<style>
  :root {
    --page-bg: #ffffff;
    --card-plum: #5a2638;
    --card-cream: #f0dfb4;
    --card-shadow: rgba(0, 0, 0, 0.18);
  }
  * { box-sizing: border-box; margin: 0; padding: 0; }
  html, body {
    width: 1200px;
    height: 900px;
    overflow: hidden;
    background: var(--page-bg);
  }
  .sheet {
    position: relative;
    width: 1200px;
    height: 900px;
    display: flex;
    align-items: center;
    justify-content: center;
    gap: 40px;
  }
  .card {
    position: relative;
    width: 540px;
    height: 312px;
    background: var(--card-plum);
    box-shadow: 0 2px 6px var(--card-shadow);
    color: var(--card-cream);
    font-family: "PT Sans", Arial, sans-serif;
  }
  .brand {
    position: absolute;
    left: 0;
    right: 0;
    text-align: center;
    font-size: 34px;
    font-weight: 400;
    letter-spacing: 0.5px;
    color: var(--card-cream);
  }
  .card-front .brand { top: 92px; }
  .card-back .brand { top: 136px; font-size: 38px; }
  .contact,
  .address {
    position: absolute;
    bottom: 22px;
    text-align: right;
    font-size: 15.5px;
    line-height: 23px;
    white-space: nowrap;
  }
  .contact { right: 250px; }
  .address { right: 18px; }
</style>
</head>
<body>
  <main class="sheet">
    <section class="card card-front" aria-label="Card front">
      <h1 class="brand">The Velvet Cupboard</h1>
      <div class="contact">
        <p class="contact-mobile">Mobile: 0412 905 261</p>
        <p class="contact-email">thevelvetcupboard@mailbox.com.au</p>
        <p class="contact-web">www.thevelvetcupboard.com.au</p>
      </div>
      <div class="address">
        <p class="address-name">Joanna Whitfield</p>
        <p class="address-street">42/871 Dunmore St, Glenwick,</p>
        <p class="address-city">Northvale, NSW, 2741</p>
      </div>
    </section>
    <section class="card card-back" aria-label="Card back">
      <p class="brand">The Velvet Cupboard</p>
    </section>
  </main>
</body>
</html>
```